we can communicate on this, but i want to follow the approach we took on Pell|Quorn & Tillet but i feel the card front needs the black background and the platinum and gold logo. The back? I am open. we can use the same info from PQ&T. Vellum Crest is an enhanced equity investment fund - basically a very exclusive boutique hedge fund that uses only stock options. very advanced things. hope you are interested

Contact Information for Business Card

Dr. Owen T. Brisket, CFA
Scientifique de fusée financière
555.014.2296
TheDoc4793@mailvessel.example

4718 Fennel Brook Way N.
West Fargo, ND 58078

No web site

Colors

Designer to choose colors to be used in the design.

Requirements
Nice to have
• I tend to prefer the most visible applications of the logo to include logo and name, the logo version with a black background and the gold and platinum components separated by the black. I see this working well for a single side (logo and name - this is card front to me).
• I am fairly open to other treatments on the reverse side with the data. To me, it makes sense to have a different color rendition of the logo on the reverse and it may be a muted black tone on tone or an oversized portion that would have spot UV. Or, the reverse may play with colors and layout
Should not have
• Other colors = no no
• Decorative font

```html
<!DOCTYPE html>
<html lang="en">
<head>
<meta charset="utf-8">
<title>Vellum Crest — Business Card</title>
<link href="https://fonts.googleapis.com/css2?family=Montserrat:wght@400;600;700&family=Roboto:wght@400&display=swap" rel="stylesheet">
<style>
  :root {
    --backdrop: #d3d3d3;
    --card-black: #141414;
    --band-dark: #232428;
    --card-white: #ffffff;
    --gold: #c9a332;
    --ink: #1b1b1b;
    --body-grey: #4a4a4a;
    --shadow: rgba(0,0,0,0.28);
  }
  * { box-sizing: border-box; margin: 0; padding: 0; }
  html, body {
    width: 1200px; height: 852px; overflow: hidden;
    background: radial-gradient(ellipse at 60% 40%, #e2e2e2 0%, var(--backdrop) 70%);
  }
  .stage { position: relative; width: 1200px; height: 852px; }

  .card {
    position: absolute;
    width: 540px; height: 309px;
    border-radius: 18px;
    overflow: hidden;
    box-shadow: 0 10px 26px var(--shadow);
  }

  /* Front */
  .card-front { left: 40px; top: 160px; background: var(--card-black); }
  .front-mark {
    position: absolute; left: 0; right: 0; top: 78px;
    display: flex; flex-direction: column; align-items: center; gap: 22px;
  }
  .mark-dot {
    width: 78px; height: 78px; border-radius: 50%;
    background: var(--gold);
  }
  .brand-name {
    font-family: "Montserrat", sans-serif;
    font-weight: 700;
    letter-spacing: 2px;
    text-transform: uppercase;
    white-space: nowrap;
  }
  .card-front .brand-name { color: #ffffff; font-size: 34px; }

  /* Back */
  .card-back { left: 620px; top: 400px; background: var(--card-white); }
  .name-band {
    position: absolute; left: 0; top: 48px;
    width: 430px; height: 100px;
    background: var(--band-dark);
    clip-path: polygon(0 0, 100% 0, 92% 100%, 0 100%);
  }
  .back-dot {
    position: absolute; left: 392px; top: 30px;
    width: 86px; height: 86px; border-radius: 50%;
    background: var(--gold);
    border: 4px solid var(--card-white);
  }
  .holder { position: absolute; left: 32px; top: 72px; }
  .holder-name {
    font-family: "Montserrat", sans-serif; font-weight: 700;
    font-size: 20px; color: var(--gold); letter-spacing: 0.5px;
    white-space: nowrap;
  }
  .holder-role {
    font-family: "Montserrat", sans-serif; font-weight: 600;
    font-size: 15px; color: #ffffff; margin-top: 5px;
    white-space: nowrap;
  }
  .address {
    position: absolute; left: 56px; top: 176px;
    font-family: "Roboto", sans-serif; font-size: 13px; line-height: 17px;
    color: var(--body-grey);
  }
  .contacts {
    position: absolute; left: 56px; top: 232px; list-style: none;
    font-family: "Roboto", sans-serif; font-size: 14px; line-height: 22px;
    color: var(--ink);
  }
  .contacts li { display: flex; align-items: center; gap: 9px; white-space: nowrap; }
  .contacts svg { width: 12px; height: 12px; fill: var(--gold); flex: none; }
  .card-back .brand-name {
    position: absolute; right: 34px; top: 186px;
    color: var(--ink); font-size: 25px;
  }
</style>
</head>
<body>
<main class="stage">

  <section class="card card-front" aria-label="Card front">
    <div class="front-mark">
      <span class="mark-dot"></span>
      <h1 class="brand-name">Vellum Crest</h1>
    </div>
  </section>

  <section class="card card-back" aria-label="Card back">
    <div class="name-band"></div>
    <span class="back-dot"></span>
    <div class="holder">
      <p class="holder-name">DR. OWEN T. BRISKET, CFA</p>
      <p class="holder-role">Scientifique de fusée financière</p>
    </div>
    <p class="address">4718 Fennel Brook Way N.<br>West Fargo, ND 58078</p>
    <ul class="contacts">
      <li>
        <svg viewBox="0 0 24 24"><path d="M6.6 10.8a15.1 15.1 0 0 0 6.6 6.6l2.2-2.2c.3-.3.7-.4 1-.2 1.1.4 2.3.6 3.6.6.6 0 1 .4 1 1V20c0 .6-.4 1-1 1A17 17 0 0 1 3 4c0-.6.4-1 1-1h3.5c.6 0 1 .4 1 1 0 1.3.2 2.5.6 3.6.1.3 0 .7-.2 1z"/></svg>
        555.014.2296
      </li>
      <li>
        <svg viewBox="0 0 24 24"><path d="M2 5h20v14H2zm2 2v.5l8 5 8-5V7z"/></svg>
        TheDoc4793@mailvessel.example
      </li>
    </ul>
    <h2 class="brand-name">Vellum Crest</h2>
  </section>

</main>
</body>
</html>
```